Child sleep consultant needs a flyer to attract new clients

We need a flyer that will attract the attention of parents with children between newborn and 3 years old who may be experiencing sleep issues. The flyer will be placed at places such as community centres, doctors room, play centres, etc.

Our business is called Hushwood Nestlings and provides a sleep consultancy service. Our service essentially provides a routine for parents to follow and general advice. Our service is not medical advice.

We need the flyer to have an overall tone that is soft and peaceful however can catch the attention of parents who may be struggling on minimal sleep. We would like photos with minimal text. The colour we use is green.

We will provide the text to appear in the flyer once we have a better idea of the layout that we prefer for the flyer. The text however wont be extensive, just some catchy points.

We want to direct people to our website which is hushwoodnestlings.com.au. We also have a facebook page, which is Hushwood Nestlings.

We have a logo that we would like to appear on the flyer. We will attach the file once the uploader on pixel bazaar is fixed.

Our consultant is a certified Dream Anchor consultant, which has a separate logo that should appear somewhere on the logo. I will attach this once the uploader is fixed.

When we print the flyer - we want to print A5 SIZE ... please make sure the formatting is OK for this size.

Target Market(s)

Mums and Dads with children between newborn and 3 years old.

Industry/Entity Type

Consultant

Colors
cadf82

Requirements
Must have
• - Our logo.
• - Dream Anchor consultant logo - both attached to this brief.
• - Contact details - including phone number, email address and website
• - MUST be suitable for A5 printable size, double sided please.
• Must have the following text:
• If your baby or toddler isn't sleeping through the night, neither are you - and this means you are probably feeling physically and mentally exhausted, stressed, depressed and irritable, afraid you might be damaging your child and disconnected from your partner.
• The good news is nearly all healthy children 3 months or older are physically capable of sleeping 12 solid hours without waking. They just need to be taught the healthy sleep habits that enable them to do so.
• I can help with the sleep issues your child is experiencing. As a certified Dream Anchor (insert trademark TM here) I can help if:
• - your child will only fall asleep when nursing or bottle feeding
• - your child needs a dummy in order fall asleep
• - you're waking up with your child one or more times per night
• - your child needs to be rocked, patted, or taken for a car ride to go to sleep
• - your own lack of sleep is starting to take a toll on your family
• I've been personally trained by Marla Penwick, best selling author of the Dream Anchor (insert trade mark symbol here) Program to teach her sleep training methods to families like yours. Marla's methods have already helped over 30,000 parents and children and I'd be delighted to help your family next!
• Call or email for a free 15 minute consultation
• I would love to connect with you to talk about your child's specific situation and discuss different solutions.

```html
<!DOCTYPE html>
<html lang="en">
<head>
<meta charset="utf-8">
<title>Hushwood Nestlings – A5 Flyer</title>
<link href="https://fonts.googleapis.com/css2?family=Cabin:ital,wght@0,400;0,500;0,600;1,400;1,600&display=swap" rel="stylesheet">
<style>
  :root {
    --green: #9fbd62;
    --green-light: #cadf82;
    --green-deep: #8aab52;
    --cream-line: #f4f1c4;
    --text-grey: #6b6b6b;
    --text-dark: #555;
    --white: #ffffff;
    --page-bg: #e9e8e4;
    --badge-blue: #9cc3e4;
  }
  * { box-sizing: border-box; margin: 0; padding: 0; }
  html, body { width: 1200px; height: 859px; overflow: hidden; }
  body {
    background: var(--page-bg);
    font-family: "Cabin", sans-serif;
    color: var(--text-grey);
    position: relative;
  }
  .flyer {
    position: absolute;
    width: 524px;
    height: 738px;
    background: var(--white);
    box-shadow: 0 4px 14px rgba(0,0,0,.18);
    overflow: hidden;
  }
  .flyer--front { left: 52px; top: 48px; }
  .flyer--back { left: 624px; top: 72px; }
  .flyer__art { position: absolute; inset: 0; }

  .social {
    position: absolute;
    display: flex; align-items: center; gap: 6px;
    font-size: 13px; color: #333;
  }
  .social__dot { width: 20px; height: 20px; border-radius: 50%; background: var(--green); }
  .flyer--front .social { right: 14px; top: 20px; }
  .flyer--back .social { left: 28px; top: 20px; }

  .headline {
    position: absolute; left: 22px; top: 50px;
    font-size: 37px; font-weight: 400; line-height: 1.1;
    color: var(--green);
  }
  .intro {
    position: absolute; left: 22px; top: 140px; width: 160px;
    font-size: 11.5px; font-style: italic; line-height: 1.35;
    color: var(--text-dark);
  }

  .brand {
    position: absolute; display: flex; align-items: center; gap: 10px;
    color: var(--green); font-size: 26px; font-weight: 400; line-height: 0.95;
  }
  .brand__circle { width: 46px; height: 46px; border-radius: 50%; background: var(--green-light); flex: none; }
  .flyer--front .brand { left: 46px; top: 400px; }

  .body-copy { position: absolute; left: 46px; top: 542px; width: 446px; }
  .body-copy__lead { font-size: 14px; color: var(--green-deep); margin-bottom: 2px; }
  .body-copy p { font-size: 10.2px; line-height: 1.35; text-align: justify; color: var(--text-dark); }
  .body-copy p + p { margin-top: 12px; }
  .body-copy .accent { color: var(--green-deep); }
  .certified { display: flex; align-items: center; justify-content: space-between; margin-top: 12px; }
  .certified p { margin: 0; }
  .badge { width: 70px; height: 34px; border-radius: 6px; background: var(--badge-blue); opacity: .55; }

  .footer {
    position: absolute; left: 0; right: 0; bottom: 0; height: 72px;
    color: var(--white); text-align: center;
  }
  .footer__cta { font-size: 16.5px; font-style: italic; font-weight: 600; margin-top: 6px; }
  .contact {
    display: flex; justify-content: center; gap: 18px; margin-top: 9px;
    font-size: 12px;
  }
  .contact span { display: flex; align-items: center; gap: 4px; }
  .contact svg { width: 11px; height: 11px; }

  .flyer--back .brand { left: 368px; top: 302px; font-size: 21px; flex-direction: column; gap: 4px; text-align: center; }
  .flyer--back .brand__circle { width: 26px; height: 26px; }

  .help { position: absolute; left: 40px; top: 468px; width: 460px; }
  .help__title { font-size: 15px; color: var(--green-deep); font-weight: 400; margin-bottom: 8px; }
  .help__list { list-style: none; }
  .help__list li {
    display: flex; align-items: center; gap: 8px;
    font-size: 13px; color: var(--text-grey); line-height: 1.42;
  }
  .help__list svg { width: 9px; height: 9px; flex: none; }
  .testimonial {
    position: absolute; left: 40px; top: 606px; width: 460px;
    font-size: 9.6px; font-style: italic; line-height: 1.3; color: var(--text-dark);
  }
</style>
</head>
<body>

<!-- Front side -->
<section class="flyer flyer--front">
  <svg class="flyer__art" width="524" height="738" viewBox="0 0 524 738">
    <defs>
      <linearGradient id="frontPhoto" x1="0" y1="0" x2="1" y2="0">
        <stop offset="0" stop-color="#ffffff"/>
        <stop offset="0.35" stop-color="#f1efec"/>
        <stop offset="0.65" stop-color="#efdccd"/>
        <stop offset="1" stop-color="#e2c8b4"/>
      </linearGradient>
    </defs>
    <path role="img" aria-label="Photo of a laughing baby wrapped in a white hooded towel" d="M0 0 H524 V408 Q150 410 0 176 Z" fill="url(#frontPhoto)"/>
    <path d="M0 176 Q150 410 524 408 V440 Q140 440 0 206 Z" fill="var(--green-light)"/>
    <path d="M0 176 Q150 410 524 408 V416 Q146 418 0 184 Z" fill="var(--green)"/>
    <path d="M0 684 Q262 628 524 684" fill="none" stroke="var(--cream-line)" stroke-width="4"/>
    <path d="M0 690 Q262 634 524 690 V738 H0 Z" fill="var(--green)"/>
  </svg>

  <div class="social"><span class="social__dot"></span>Hushwood Nestlings</div>

  <h1 class="headline">Get Baby<br>to sleep!</h1>
  <p class="intro">I would love to connect with you to talk about your child's specific situation and discuss different solutions.</p>

  <div class="brand"><span class="brand__circle"></span><span>hushwood<br>nestlings</span></div>

  <div class="body-copy">
    <h2 class="body-copy__lead">If your baby or toddler isn't sleeping through the night, neither are you</h2>
    <p>and this means you are probably feeling physically and mentally exhausted, stressed, depressed and irritable, afraid you might be damaging your child and disconnected from your partner.</p>
    <p><span class="accent">The good news</span> is nearly all healthy children 3 months or older are physically capable of sleeping 12 solid hours without waking. They just need to be taught the healthy sleep habits that enable them to do so.</p>
    <div class="certified">
      <p>I can help with the sleep issues your child is experiencing. As a certified Dream Anchor™</p>
      <span class="badge"></span>
    </div>
  </div>

  <footer class="footer">
    <p class="footer__cta">Contact us today for your free 15 minute consultation.</p>
    <div class="contact">
      <span><svg viewBox="0 0 12 12"><path d="M3 1 L5 3.5 L4 5 Q5 7 7 8 L8.5 7 L11 9 L9.5 11 Q5 11 1 4 Z" fill="none" stroke="#fff" stroke-width="1"/></svg>0400 555 019</span>
      <span><svg viewBox="0 0 12 12"><circle cx="6" cy="6" r="5" fill="none" stroke="#fff"/><circle cx="6" cy="6" r="2" fill="none" stroke="#fff"/></svg>tess@hushwoodnestlings.com.au</span>
      <span><svg viewBox="0 0 12 12"><circle cx="6" cy="6" r="5" fill="none" stroke="#fff"/><path d="M6 5 V9 M6 3 V3.8" stroke="#fff"/></svg>hushwoodnestlings.com.au</span>
    </div>
  </footer>
</section>

<!-- Back side -->
<section class="flyer flyer--back">
  <svg class="flyer__art" width="524" height="738" viewBox="0 0 524 738">
    <defs>
      <linearGradient id="backPhoto" x1="0" y1="0" x2="1" y2="1">
        <stop offset="0" stop-color="#e8e2da"/>
        <stop offset="0.5" stop-color="#e6cfbf"/>
        <stop offset="1" stop-color="#efebe4"/>
      </linearGradient>
    </defs>
    <path role="img" aria-label="Photo of a newborn baby sleeping on a soft white blanket" d="M0 0 H524 V150 Q430 440 0 420 Z" fill="url(#backPhoto)"/>
    <path d="M0 420 Q430 440 524 150 V200 Q440 470 0 450 Z" fill="var(--green-light)"/>
    <path d="M0 420 Q430 440 524 150 V162 Q434 452 0 428 Z" fill="var(--green)"/>
    <circle cx="422" cy="342" r="76" fill="var(--white)" stroke="var(--green)" stroke-width="8"/>
    <path d="M0 684 Q262 628 524 684" fill="none" stroke="var(--cream-line)" stroke-width="4"/>
    <path d="M0 690 Q262 634 524 690 V738 H0 Z" fill="var(--green)"/>
  </svg>

  <div class="social"><span class="social__dot"></span>Hushwood Nestlings</div>

  <div class="brand"><span class="brand__circle"></span><span>hushwood<br>nestlings</span></div>

  <div class="help">
    <h2 class="help__title">I CAN HELP IF:</h2>
    <ul class="help__list">
      <li><svg viewBox="0 0 10 10"><circle cx="5" cy="5" r="5" fill="var(--green)"/><path d="M4 3 L6 5 L4 7" fill="none" stroke="#fff" stroke-width="1.2"/></svg>your child will only fall asleep when nursing or bottle feeding</li>
      <li><svg viewBox="0 0 10 10"><circle cx="5" cy="5" r="5" fill="var(--green)"/><path d="M4 3 L6 5 L4 7" fill="none" stroke="#fff" stroke-width="1.2"/></svg>your child needs a dummy in order fall asleep</li>
      <li><svg viewBox="0 0 10 10"><circle cx="5" cy="5" r="5" fill="var(--green)"/><path d="M4 3 L6 5 L4 7" fill="none" stroke="#fff" stroke-width="1.2"/></svg>you're waking up with your child one or more times per night</li>
      <li><svg viewBox="0 0 10 10"><circle cx="5" cy="5" r="5" fill="var(--green)"/><path d="M4 3 L6 5 L4 7" fill="none" stroke="#fff" stroke-width="1.2"/></svg>your child needs to be rocked, patted, or taken for a car ride to go to sleep</li>
      <li><svg viewBox="0 0 10 10"><circle cx="5" cy="5" r="5" fill="var(--green)"/><path d="M4 3 L6 5 L4 7" fill="none" stroke="#fff" stroke-width="1.2"/></svg>your own lack of sleep is starting to take a toll on your family</li>
    </ul>
  </div>

  <p class="testimonial">- I've been personally trained by Marla Penwick, best selling author of the Dream Anchor Program to teach her sleep training methods to families like yours. Marla's methods have already helped over 30,000 parents and children and I'd be delighted to help your family next!</p>

  <footer class="footer">
    <p class="footer__cta">Contact us today for your free 15 minute consultation.</p>
    <div class="contact">
      <span><svg viewBox="0 0 12 12"><path d="M3 1 L5 3.5 L4 5 Q5 7 7 8 L8.5 7 L11 9 L9.5 11 Q5 11 1 4 Z" fill="none" stroke="#fff" stroke-width="1"/></svg>0400 555 019</span>
      <span><svg viewBox="0 0 12 12"><circle cx="6" cy="6" r="5" fill="none" stroke="#fff"/><circle cx="6" cy="6" r="2" fill="none" stroke="#fff"/></svg>tess@hushwoodnestlings.com.au</span>
      <span><svg viewBox="0 0 12 12"><circle cx="6" cy="6" r="5" fill="none" stroke="#fff"/><path d="M6 5 V9 M6 3 V3.8" stroke="#fff"/></svg>hushwoodnestlings.com.au</span>
    </div>
  </footer>
</section>

</body>
</html>
```